Marwick Agency (http://mk.fennoweb-studio.com/)

We are looking for a similar design to what we have, but more professional looking and cleaned up with links and logo that is not so grainy looking. We are an independent insurance agency marketing to personal and commercial clients. We offer all commercial lines markets and all personal lines. We target excavators, landscapers, restaurants, golf courses, contractors. Please look at http://mk.fennoweb-studio.com/ which we had designed but do not like it, it will give you an idea of what we are looking for.

Target Market(s)

Commercial and personal insurance. All business products and all personal (homeowners, auto, antique auto, umbrella)

Industry/Entity Type

It Professional

Logo Text

Knowledge Building Your Assurance

Number of Pages Required

5+ page

Colors
000000
848484
0255a3

```html
<!DOCTYPE html>
<html lang="en">
<head>
<meta charset="utf-8">
<title>Marwick Agency</title>
<link href="https://fonts.googleapis.com/css2?family=Open+Sans:wght@400;600;700&family=Oswald:wght@500&display=swap" rel="stylesheet">
<style>
:root{
  --brand:#0b3d91;
  --brand-deep:#072a66;
  --ink:#333;
  --muted:#555;
  --grey:#848484;
  --panel:#efefef;
  --partners-bg:#e4e4e4;
  --footer-bg:#222;
  --line:#d6d6d6;
}
*{box-sizing:border-box;margin:0;padding:0}
html,body{width:1200px;height:2214px;overflow:hidden}
body{font-family:'Open Sans',Arial,sans-serif;color:var(--ink);background:#fff;position:relative}
.abs{position:absolute}

/* header */
.site-header{position:absolute;left:0;top:0;width:1200px;height:168px;border-top:3px solid #666;background:#fff}
.call-tab{position:absolute;left:818px;top:0;width:284px;height:40px;background:#757575;color:#fff;font-weight:600;font-size:14px;display:flex;align-items:center;justify-content:center;clip-path:polygon(0 0,100% 0,94% 100%,6% 100%)}
.brand{position:absolute;left:98px;top:54px;display:flex;align-items:center;gap:12px;font-size:30px;font-weight:700;color:var(--brand)}
.brand-dot{width:26px;height:26px;border-radius:50%;background:var(--brand)}
.main-nav{position:absolute;right:99px;top:100px;display:flex;border-top:2px solid var(--brand);height:40px;align-items:center}
.main-nav a{font-size:11.5px;font-weight:600;color:#333;text-decoration:none;padding:0 16px;border-left:1px solid #ccc;line-height:14px;text-transform:uppercase}
.main-nav a:nth-child(2){border-left:none}
.main-nav a.active{background:var(--brand);color:#fff;border:none;height:50px;line-height:44px;margin-top:6px;padding:0 14px;clip-path:polygon(0 0,100% 0,100% 78%,50% 100%,0 78%)}

/* hero */
.hero{position:absolute;left:0;top:168px;width:1200px;height:514px;background:linear-gradient(180deg,#1f3554 0%,#223a5c 45%,#0f1e36 100%)}
.hero-arrow{position:absolute;top:232px;width:44px;height:44px;border-radius:50%;background:rgba(255,255,255,.25)}
.hero h1{position:absolute;top:322px;width:100%;text-align:center;color:#fff;font-size:27px;font-weight:700;letter-spacing:.3px}
.hero p{position:absolute;top:364px;left:300px;width:600px;text-align:center;color:#fff;font-size:17px;line-height:29px}

/* services */
.section-title{color:var(--brand);font-size:20px;font-weight:700;text-transform:uppercase}
.services-title{left:98px;top:733px}
.services-intro{left:98px;top:772px;font-size:12px;color:var(--muted)}
.service{position:absolute;top:823px;width:232px}
.service .photo{height:174px;box-shadow:0 4px 5px rgba(0,0,0,.25)}
.service h3{margin-top:22px;font-size:14px;font-weight:700;color:#333;text-transform:uppercase}
.service p{margin-top:8px;font-size:11.5px;line-height:21px;color:#444;width:205px}

/* about band */
.about{position:absolute;left:0;top:1145px;width:1200px;height:325px;background:linear-gradient(180deg,#2f3638,#1c2224 60%,#15191a)}
.about h2{position:absolute;top:70px;width:100%;text-align:center;color:#fff;font-size:19px;font-weight:700}
.about p{position:absolute;top:116px;left:160px;width:880px;text-align:center;color:#fff;font-size:11.5px;line-height:24px}
.btn-outline{position:absolute;left:507px;top:213px;width:187px;height:47px;border:2px solid #fff;color:#fff;font-size:12px;font-weight:700;display:flex;align-items:center;justify-content:center}

/* target */
.target-title{top:1527px;width:1200px;text-align:center}
.target-intro{top:1566px;left:200px;width:800px;text-align:center;font-size:14px;line-height:28px;color:#444}
.targets{position:absolute;left:98px;top:1653px;width:1003px;height:230px;display:flex;gap:2px}
.target{flex:1;background:var(--panel);display:flex;flex-direction:column;align-items:center;position:relative}
.target h4{margin-top:20px;font-size:14px;font-weight:700;color:#333;text-transform:uppercase;line-height:18px}
.target .icon{margin-top:20px;height:50px;display:flex;align-items:center;justify-content:center}
.target p{margin-top:24px;width:180px;text-align:center;font-size:11.5px;line-height:20px;color:#333}
.target .more{position:absolute;bottom:0;left:0;right:0;height:38px;background:#8c8c8c;color:#fff;font-size:9px;font-weight:700;display:flex;align-items:center;justify-content:center;text-transform:uppercase}
.target.active{background:var(--brand)}
.target.active h4,.target.active p{color:#fff}
.target.active .more{background:var(--brand-deep)}

/* partners */
.partners{position:absolute;left:0;top:1948px;width:1200px;height:162px;background:var(--partners-bg);display:flex;justify-content:space-between;align-items:center;padding:0 99px}
.partner{font-family:'Oswald','Open Sans',sans-serif;font-size:28px;font-weight:500;color:#9a9a9a}

/* footer */
.site-footer{position:absolute;left:0;top:2110px;width:1200px;height:104px;background:var(--footer-bg);color:#bbb}
.footer-links{position:absolute;left:98px;top:32px;font-size:10.5px;text-transform:uppercase}
.footer-links span{margin:0 10px;color:#888}
.copyright{position:absolute;left:98px;top:62px;font-size:10px}
.social{position:absolute;left:732px;top:36px;display:flex;align-items:center;gap:6px;font-size:9px;text-transform:uppercase}
.social i{display:block;width:32px;height:32px;border:1px solid #777;border-radius:50%;margin-left:4px}
</style>
</head>
<body>

<header class="site-header">
  <div class="call-tab">Call US Today ! &nbsp;1-888-4 Marwick</div>
  <div class="brand"><span class="brand-dot"></span>Marwick Agency</div>
  <nav class="main-nav">
    <a class="active">Home</a>
    <a>Personal Insurance</a>
    <a>Business Insurance</a>
    <a>Service Center</a>
    <a>About Us</a>
    <a>Contact Us</a>
  </nav>
</header>

<section class="hero" role="img" aria-label="Team of business people in suits standing in front of a world map">
  <span class="hero-arrow" style="left:28px"></span>
  <span class="hero-arrow" style="right:28px"></span>
  <h1>SMALL ENOUGH TO CARE, BIG ENOUGH TO MAKE A DIFFERENCE</h1>
  <p>Please find information about our agency, its principles , and the various types of insurance coverages that we provide.</p>
</section>

<h2 class="abs section-title services-title">Our Services</h2>
<p class="abs services-intro">Es simplemente el texto de relleno de las imprentas y archivos de texto. Lorem Ipsum ha sido el texto de relleno estándar de las...</p>

<article class="service" style="left:98px">
  <div class="photo" role="img" aria-label="Business team meeting around a laptop" style="background:linear-gradient(135deg,#dfe9f2,#7b8fa5)"></div>
  <h3>Busines Insurance</h3><p>Lorem Ipsum is simply dummy text of the printing.....</p>
</article>
<article class="service" style="left:356px">
  <div class="photo" role="img" aria-label="Couple beside their car" style="background:linear-gradient(135deg,#6f8fb2,#c8a88c)"></div>
  <h3>Auto Insurance</h3><p>Lorem Ipsum is simply dummy text of the printing.....</p>
</article>
<article class="service" style="left:614px">
  <div class="photo" role="img" aria-label="Family walking in a flower meadow" style="background:linear-gradient(180deg,#bcd3e6,#6f9b3e 60%,#4f7c2a)"></div>
  <h3>Life Insurance</h3><p>Lorem Ipsum is simply dummy text of the printing.....</p>
</article>
<article class="service" style="left:871px">
  <div class="photo" role="img" aria-label="Couple in front of their house" style="background:linear-gradient(180deg,#c9d7e4,#a89076 50%,#4e8a2c)"></div>
  <h3>Home Insurance</h3><p>Lorem Ipsum is simply dummy text of the printing.....</p>
</article>

<section class="about" role="img" aria-label="People holding black umbrellas in the rain">
  <h2>ABOUT MARWICK AGENCY</h2>
  <p>Lorem Ipsum is simply dummy text of the printing and typesetting industry. Lorem Ipsum has been the industry's standard dummy text ever since the 1500s, when an unknown printer took a galley of type and scrambled it to make a type specimen book. It has survived not only five centuries, but also the leap into electronic typesetting, remaining essentially unchanged</p>
  <div class="btn-outline">READ MORE INFO</div>
</section>

<h2 class="abs section-title target-title">Our Target</h2>
<p class="abs target-intro">Lorem Ipsum is simply dummy text of the printing and typesetting industry. Lorem Ipsum has been the industry's standard dummy text ever</p>

<div class="targets">
  <div class="target active">
    <h4>Excavators</h4>
    <div class="icon"><svg width="58" height="44" viewBox="0 0 58 44" fill="none" stroke="#fff" stroke-width="3"><path d="M2 2v40h54"/><rect x="11" y="22" width="6" height="16" fill="#fff" stroke="none"/><rect x="22" y="14" width="6" height="24" fill="#fff" stroke="none"/><rect x="33" y="18" width="6" height="20" fill="#fff" stroke="none"/><rect x="44" y="8" width="6" height="30" fill="#fff" stroke="none"/></svg></div>
    <p>Lorem Ipsum is simply<br>dummy text of the printing</p>
    <div class="more">Click here for more info &nbsp;›</div>
  </div>
  <div class="target">
    <h4>Landscapers</h4>
    <div class="icon"><svg width="48" height="44" viewBox="0 0 48 44" fill="#555"><path d="M24 2 2 22h6v20h12V30h8v12h12V22h6z"/></svg></div>
    <p>Lorem Ipsum is simply<br>dummy text of the printing</p>
    <div class="more">Click here for more info &nbsp;›</div>
  </div>
  <div class="target">
    <h4>Restaurants</h4>
    <div class="icon"><svg width="40" height="50" viewBox="0 0 40 50"><rect x="2" y="0" width="36" height="50" fill="#555"/><g fill="#efefef"><rect x="8" y="6" width="5" height="5"/><rect x="17" y="6" width="5" height="5"/><rect x="26" y="6" width="5" height="5"/><rect x="8" y="15" width="5" height="5"/><rect x="17" y="15" width="5" height="5"/><rect x="26" y="15" width="5" height="5"/><rect x="8" y="24" width="5" height="5"/><rect x="17" y="24" width="5" height="5"/><rect x="26" y="24" width="5" height="5"/><rect x="16" y="38" width="8" height="12"/></g></svg></div>
    <p>Lorem Ipsum is simply<br>dummy text of the printing</p>
    <div class="more">Click here for more info &nbsp;›</div>
  </div>
  <div class="target">
    <h4>Golf Courses</h4>
    <div class="icon"><svg width="40" height="50" viewBox="0 0 40 50"><path d="M2 0h26l10 10v40H2z" fill="#555"/><g fill="#efefef"><rect x="9" y="20" width="22" height="3"/><rect x="9" y="28" width="22" height="3"/><rect x="9" y="36" width="22" height="3"/></g></svg></div>
    <p>Lorem Ipsum is simply<br>dummy text of the printing</p>
    <div class="more">Click here for more info &nbsp;›</div>
  </div>
  <div class="target">
    <h4>Contractors</h4>
    <div class="icon"><svg width="56" height="50" viewBox="0 0 56 50" fill="#555"><circle cx="28" cy="12" r="10"/><circle cx="10" cy="18" r="7"/><circle cx="46" cy="18" r="7"/><path d="M12 50c0-14 7-24 16-24s16 10 16 24z"/><path d="M0 44c0-10 4-17 10-17 3 0 5 1 7 3-3 4-5 9-5 14z"/><path d="M56 44c0-10-4-17-10-17-3 0-5 1-7 3 3 4 5 9 5 14z"/></svg></div>
    <p>Lorem Ipsum is simply<br>dummy text of the printing</p>
    <div class="more">Click here for more info &nbsp;›</div>
  </div>
</div>

<section class="partners">
  <span class="partner">Stratum</span>
  <span class="partner">Calveno</span>
  <span class="partner">Northgate</span>
  <span class="partner">Velmora</span>
  <span class="partner">Linden</span>
  <span class="partner">Brackley</span>
</section>

<footer class="site-footer">
  <div class="footer-links">Home<span>/</span>Personal Insurance<span>/</span>Business Insurance<span>/</span>Service Center<span>/</span>About Us<span>/</span>Contact Us</div>
  <div class="copyright">© 2015. MARWICK AGENCY. ALL RIGHTS RESERVED.</div>
  <div class="social">Connect with our social network : <i aria-label="Social network"></i><i aria-label="Social network"></i><i aria-label="Social network"></i><i aria-label="Social network"></i><i aria-label="Social network"></i></div>
</footer>

</body>
</html>
```